Dear Designer
I am looking for some proposal for the graphic design of our new web site
www.drelvo.com; you can find in real time the developper version on : drelvo.pokrane.info/?id=308

We do not need web page programing... no IT stuff .. only to provide me graphic contents for some pages:
- home
- contact us
- product page
- download page
- blog page
- application page
Pls advise me back asap
Thank you
Bernard

Number of Pages Required

1 page

```html
<!DOCTYPE html>
<html lang="en">
<head>
<meta charset="utf-8">
<title>Kavro – Website Pages</title>
<link href="https://fonts.googleapis.com/css2?family=Poppins:wght@300;400;500;600;700&display=swap" rel="stylesheet">
<style>
:root{
  --blue:#1c6dc5;
  --blue-dark:#1558a6;
  --blue-soft:#dce9f7;
  --ink:#2b2b2b;
  --muted:#8a8a8a;
  --line:#e4e4e4;
  --canvas:#e9e9e9;
  --bar-grey:#c9c9c9;
  --panel-grey:#f1f1f1;
  --white:#ffffff;
}
*{box-sizing:border-box;margin:0;padding:0}
html,body{width:1200px;height:2242px;overflow:hidden}
body{background:var(--canvas);font-family:'Poppins',sans-serif;color:var(--ink);position:relative}
.page{position:absolute;width:560px;background:var(--white);overflow:hidden;box-shadow:0 1px 3px rgba(0,0,0,.08)}
.abs{position:absolute}

/* top bar */
.topbar{position:absolute;left:0;top:0;width:100%;height:17px;background:var(--blue);display:flex;align-items:center;justify-content:flex-end;gap:16px;padding-right:52px;font-size:5.6px;color:var(--white)}
.topbar .social{position:absolute;left:0;top:0;width:129px;height:17px;background:var(--bar-grey);display:flex;gap:5px;align-items:center;padding-left:52px}
.dot{width:8px;height:8px;border-radius:50%;background:#8d8d8d}
.topbar .item{display:flex;align-items:center;gap:3px}
.topbar svg{width:6px;height:6px}

/* header */
.header{position:absolute;left:0;top:17px;width:100%;height:56px;border-bottom:1px solid var(--line)}
.logo{position:absolute;left:52px;top:14px;font-size:24px;font-weight:700;color:var(--blue);letter-spacing:.5px;line-height:1}
.nav{position:absolute;left:184px;top:23px;display:flex;gap:12px;font-size:6.4px;font-weight:500;color:var(--ink)}
.nav .active{color:var(--blue)}
.nav svg{width:7px;height:7px;margin-left:2px}

/* footer */
.site-footer{position:absolute;left:0;width:560px;height:215px;background:var(--blue);color:var(--white)}
.f-logo{position:absolute;left:52px;top:70px;font-size:24px;font-weight:700;color:var(--white);line-height:1}
.f-social{position:absolute;left:58px;top:106px;display:flex;gap:2px}
.ring{width:23px;height:23px;border-radius:50%;border:1px solid rgba(255,255,255,.7)}
.f-col{position:absolute;top:36px;font-size:5.6px;line-height:14px}
.f-col h4{font-size:6.2px;font-weight:500;letter-spacing:.2px;position:relative;margin-bottom:6px}
.f-col h4::after{content:"";position:absolute;left:0;bottom:-3px;width:13px;height:1px;background:var(--white)}
.f-col.contact{line-height:10px}
.f-col.contact h4{line-height:14px;margin-bottom:8px}
.f-col.contact .lbl{font-size:6px;margin-top:4px}
.f-col.contact .val{font-size:5.2px;opacity:.9}
.f-col.news{line-height:10px}
.f-col.news h4{line-height:14px;margin-bottom:8px}
.f-col.news p{font-size:5.2px;width:112px;opacity:.9}
.f-input{margin-top:10px;width:109px;height:17px;border-radius:9px;background:var(--blue-dark);box-shadow:inset 0 0 0 1px rgba(255,255,255,.35);display:flex;align-items:center;justify-content:space-between;padding:0 4px 0 9px;font-size:5.2px}
.f-input span.go{width:9px;height:9px;border-radius:50%;background:var(--white)}
.f-rule{position:absolute;left:52px;top:179px;width:456px;height:1px;background:rgba(255,255,255,.5)}
.f-bottom{position:absolute;left:52px;top:194px;width:456px;display:flex;justify-content:space-between;font-size:5.6px}

/* product page */
.sidebar{position:absolute;left:41px;top:104px;width:125px;height:288px;background:var(--panel-grey)}
.search{position:absolute;left:8px;top:18px;width:108px;height:24px;background:var(--white);border:1px solid #dcdcdc;display:flex;align-items:center;justify-content:space-between;padding:0 6px;font-size:6.4px;color:#666}
.search svg{width:7px;height:7px}
.cat-title{position:absolute;left:8px;top:68px;font-size:8.6px;font-weight:500}
.cat-list{position:absolute;left:9px;top:92px;list-style:none;font-size:7px}
.cat-list li{display:flex;align-items:center;gap:6px;height:24px}
.box{width:7px;height:7px;border-radius:1px;background:#d5d5d5}
.cat-list li.on{color:var(--blue)}
.cat-list li.on .box{background:var(--blue)}
.section-title{position:absolute;font-size:15px;font-weight:600;color:var(--blue);letter-spacing:.2px}
.p-card{position:absolute;width:112px;height:168px;background:var(--white);box-shadow:0 0 4px rgba(0,0,0,.14)}
.p-img{position:absolute;left:5px;top:5px;width:102px;height:96px}
.p-name{position:absolute;left:7px;top:108px;font-size:6.4px;font-weight:500}
.p-desc{position:absolute;left:7px;top:121px;width:100px;font-size:4.6px;line-height:10px;color:var(--muted)}
.p-price{position:absolute;left:7px;top:149px;font-size:7.4px;font-weight:500;color:var(--blue)}

/* application page */
.hero{position:absolute;left:0;top:66px;width:560px;height:381px;background:linear-gradient(180deg,#3f4752 0%,#565a5c 35%,#3b4534 68%,#1f2a1d 100%)}
.hero-band{position:absolute;left:0;top:447px;width:560px;height:92px;background:#efefef}
.hero h1{position:absolute;left:29px;top:123px;font-size:28px;font-weight:500;color:var(--white);letter-spacing:.3px}
.hero p{position:absolute;left:29px;top:162px;width:200px;font-size:6.2px;line-height:14px;color:var(--white)}
.btn{position:absolute;display:flex;align-items:center;justify-content:center;background:var(--blue);color:var(--white);font-size:6.6px;font-weight:500}
.wheel{position:absolute;left:0;top:0}
.wheel-label{position:absolute;font-size:5.6px;color:var(--white);font-weight:500;line-height:8px}
.app-card{position:absolute;left:48px;top:393px;width:460px;height:100px;background:var(--white);box-shadow:0 1px 6px rgba(0,0,0,.12)}
.app-card .app-visual{position:absolute;left:28px;top:24px;width:58px;height:52px;background:var(--blue-soft);border-radius:4px}
.app-card .divider{position:absolute;left:113px;top:16px;width:1px;height:68px;background:var(--line)}
.app-card h3{position:absolute;left:137px;top:18px;font-size:10px;font-weight:500;color:var(--blue)}
.app-card p{position:absolute;left:137px;top:39px;width:305px;font-size:6.1px;line-height:15px;color:var(--muted)}
.arrow-c{position:absolute;width:15px;height:15px;border-radius:50%;border:1px solid var(--white);display:flex;align-items:center;justify-content:center}
.arrow-c svg{width:7px;height:7px}

/* blog */
.center-title{position:absolute;left:0;width:560px;text-align:center;font-size:15px;font-weight:600;color:var(--blue)}
.center-title span{display:inline-block;width:26px;height:1px;background:var(--blue);vertical-align:middle;margin:0 6px}
.center-sub{position:absolute;left:0;width:560px;text-align:center;font-size:6.4px;line-height:12px;color:#555}
.b-card{position:absolute;width:200px;height:291px;background:var(--white);box-shadow:0 0 4px rgba(0,0,0,.16)}
.b-img{position:absolute;left:0;top:0;width:200px;height:137px}
.b-meta{position:absolute;left:9px;top:149px;display:flex;align-items:center;gap:5px;font-size:6.1px;color:#444}
.avatar{width:17px;height:17px;border-radius:50%;background:#555}
.kebab{position:absolute;right:11px;top:151px;width:2px;height:11px;background:radial-gradient(circle,#444 1px,transparent 1.2px) 0 0/2px 4px repeat-y}
.b-title{position:absolute;left:11px;top:180px;width:182px;font-size:6.3px;font-weight:600;line-height:12px;text-transform:uppercase}
.b-text{position:absolute;left:11px;top:209px;width:182px;font-size:5.3px;line-height:11.5px;color:var(--muted)}
.b-rule{position:absolute;left:11px;top:266px;width:178px;height:1px;background:var(--line)}
.b-foot{position:absolute;left:16px;top:276px;width:170px;display:flex;justify-content:space-between;font-size:5.4px;color:var(--muted)}
.b-foot small{font-size:3.6px}

/* downloads */
.d-img{position:absolute;width:232px;height:173px}
.d-card{position:absolute;width:221px;height:143px;background:var(--white);box-shadow:0 0 6px rgba(0,0,0,.14)}
.d-card h3{position:absolute;left:23px;top:17px;font-size:10.4px;font-weight:500}
.d-card .tag{position:absolute;left:23px;top:35px;font-size:5.8px;color:var(--blue)}
.d-card p{position:absolute;left:23px;top:54px;width:185px;font-size:5.6px;line-height:12px;color:#666}
.d-card .btn{left:23px;top:101px;width:72px;height:22px}
</style>
</head>
<body>

<!-- PRODUCT PAGE -->
<section class="page" style="left:29px;top:52px;height:770px">
  <div class="topbar">
    <div class="social"><span class="dot"></span><span class="dot"></span><span class="dot"></span></div>
    <span class="item"><svg viewBox="0 0 10 10"><path d="M2 1l2 2-1 1.5c.8 1.5 1.5 2.2 3 3L7.5 6l2 2L8 9.5C4 9 1 6 .5 2z" fill="#fff"/></svg>+ (1) 555 014 2290</span>
    <span class="item"><svg viewBox="0 0 10 10"><rect x="0" y="2" width="10" height="6" fill="#fff"/></svg>hello@kavrodrive.com</span>
    <span class="item">Select language: <span class="dot" style="width:6px;height:6px;background:#fff"></span> Eng ▾</span>
  </div>
  <div class="header">
    <div class="logo">Kavro</div>
    <nav class="nav"><span>Home</span><span class="active">Product</span><span>Applications</span><span>Company</span><span>Downloads</span><span>Blog</span><span>Contact</span><span>Contact</span><svg viewBox="0 0 10 10"><circle cx="4" cy="4" r="3" fill="none" stroke="#333" stroke-width="1.4"/><path d="M6.3 6.3L9 9" stroke="#333" stroke-width="1.4"/></svg></nav>
  </div>

  <aside class="sidebar">
    <div class="search">Search <svg viewBox="0 0 10 10"><circle cx="4" cy="4" r="3" fill="none" stroke="#333" stroke-width="1.4"/><path d="M6.3 6.3L9 9" stroke="#333" stroke-width="1.4"/></svg></div>
    <div class="cat-title">Categories</div>
    <ul class="cat-list">
      <li class="on"><span class="box"></span>V-Belts</li>
      <li><span class="box"></span>Ribbed Belts</li>
      <li><span class="box"></span>Timing Belts</li>
      <li><span class="box"></span>Thermowledable Belts</li>
      <li><span class="box"></span>Agri-Belts</li>
    </ul>
  </aside>

  <h2 class="section-title" style="left:177px;top:124px">OUR PRODUCTS</h2>

  <article class="p-card" style="left:177px;top:159px"><div class="p-img" role="img" aria-label="Engine belt drive close-up" style="background:linear-gradient(135deg,#6b6b6b,#1e1e1e)"></div><div class="p-name">WRAPPED</div><div class="p-desc">Lorem ipsum dolor sit amet, adipiscing elit, sed do eiusmod tempor</div><div class="p-price">$150.00</div></article>
  <article class="p-card" style="left:294px;top:159px"><div class="p-img" role="img" aria-label="Cogged raw edge belt close-up" style="background:linear-gradient(135deg,#d9d9d9,#2a2a2a)"></div><div class="p-name">COGGED RAW EDGE</div><div class="p-desc">Lorem ipsum dolor sit amet, adipiscing elit, sed do eiusmod tempor</div><div class="p-price">$150.00</div></article>
  <article class="p-card" style="left:411px;top:159px"><div class="p-img" role="img" aria-label="Timing gears with banded belt" style="background:linear-gradient(135deg,#8a8a8a,#333)"></div><div class="p-name">BANDED</div><div class="p-desc">Lorem ipsum dolor sit amet, adipiscing elit, sed do eiusmod tempor</div><div class="p-price">$150.00</div></article>
  <article class="p-card" style="left:177px;top:339px"><div class="p-img" role="img" aria-label="Belt kit with pulleys" style="background:radial-gradient(circle,#d8d8d8,#efefef)"></div><div class="p-name">NETLINK V-BELT</div><div class="p-desc">Lorem ipsum dolor sit amet, adipiscing elit, sed do eiusmod tempor</div><div class="p-price">$150.00</div></article>
  <article class="p-card" style="left:294px;top:339px"><div class="p-img" role="img" aria-label="Variable speed belt loop" style="background:radial-gradient(circle,#bdbdbd,#f2f2f2)"></div><div class="p-name">VARIABLE SPEED BELTS</div><div class="p-desc">Lorem ipsum dolor sit amet, adipiscing elit, sed do eiusmod tempor</div><div class="p-price">$150.00</div></article>

  <footer class="site-footer" style="top:555px">
    <div class="f-logo">Kavro</div>
    <div class="f-social"><span class="ring"></span><span class="ring"></span></div>
    <div class="f-col" style="left:143px"><h4>QUICK LINKS</h4>Home<br>Product<br>Applications<br>Company<br>Downloads<br>Blog<br>Contact</div>
    <div class="f-col" style="left:217px"><h4>PRODUCT</h4>V-Belts<br>Ribbed Belts<br>Timing Belts<br>Thermowledable Belts<br>Agri-Belts</div>
    <div class="f-col contact" style="left:305px"><h4>CONTACT US</h4><div class="lbl">ADDRESS</div><div class="val">48 Maple Ridge Lane<br>Oakvale, ON K2P 5R1</div><div class="lbl">PHONE</div><div class="val">+ (1) 555 014 2290</div><div class="lbl">EMAIL</div><div class="val">hello@kavrodrive.com</div></div>
    <div class="f-col news" style="left:406px"><h4>NEWSLETTER</h4><p>Lorem ipsum dolor sit amet, consectetur adipiscing elit, sed do eiusmod tempor</p><div class="f-input">Enter Email <span class="go"></span></div></div>
    <div class="f-rule"></div>
    <div class="f-bottom"><span>© 2021 All Rights Reserved</span><span>PRIVACY POLICY / &nbsp;TERMS &amp; CONDITION</span></div>
  </footer>
</section>

<!-- APPLICATION PAGE -->
<section class="page" style="left:611px;top:52px;height:753px">
  <div class="topbar">
    <div class="social"><span class="dot"></span><span class="dot"></span><span class="dot"></span></div>
    <span class="item"><svg viewBox="0 0 10 10"><path d="M2 1l2 2-1 1.5c.8 1.5 1.5 2.2 3 3L7.5 6l2 2L8 9.5C4 9 1 6 .5 2z" fill="#fff"/></svg>+ (1) 555 014 2290</span>
    <span class="item"><svg viewBox="0 0 10 10"><rect x="0" y="2" width="10" height="6" fill="#fff"/></svg>hello@kavrodrive.com</span>
    <span class="item">Select language: <span class="dot" style="width:6px;height:6px;background:#fff"></span> Eng ▾</span>
  </div>
  <div class="header" style="height:49px">
    <div class="logo" style="top:11px">Kavro</div>
    <nav class="nav" style="top:20px"><span>Home</span><span>Product</span><span class="active">Applications</span><span>Company</span><span>Downloads</span><span>Blog</span><span>Contact</span><span>Contact</span><svg viewBox="0 0 10 10"><circle cx="4" cy="4" r="3" fill="none" stroke="#333" stroke-width="1.4"/><path d="M6.3 6.3L9 9" stroke="#333" stroke-width="1.4"/></svg></nav>
  </div>

  <div class="hero" role="img" aria-label="Power transmission tower over forest at dusk"></div>
  <div class="hero-band"></div>
  <div class="hero" style="background:none">
    <h1>APPLICATION</h1>
    <p>Kavro Drive Systems designs, engineers, produces, and distributes high-quality power transmission</p>
    <div class="btn" style="left:29px;top:197px;width:71px;height:23px">GET STARTED</div>
  </div>

  <svg class="wheel" width="560" height="460" viewBox="0 0 560 460">
    <circle cx="377" cy="248" r="100" fill="none" stroke="#fff" stroke-opacity=".6" stroke-width="1" stroke-dasharray="2 3"/>
    <circle cx="377" cy="248" r="65" fill="#1c6dc5"/>
    <g fill="#fff">
      <circle cx="377" cy="147" r="15" fill="#1c6dc5" stroke="#fff" stroke-width="2"/>
      <circle cx="452" cy="177" r="15"/><circle cx="475" cy="248" r="15"/><circle cx="448" cy="310" r="15"/>
      <circle cx="377" cy="339" r="15"/><circle cx="307" cy="315" r="15"/><circle cx="279" cy="248" r="15"/><circle cx="303" cy="177" r="15"/>
    </g>
    <g fill="none" stroke="#1c6dc5" stroke-width="1.2">
      <rect x="446" y="171" width="12" height="12" rx="2"/><rect x="469" y="242" width="12" height="12"/><path d="M442 316l6-10 6 10z"/>
      <path d="M371 335l6-4 6 4v8l-6 3-6-3z"/><circle cx="307" cy="315" r="6"/><rect x="273" y="244" width="12" height="8"/><rect x="297" y="171" width="12" height="12"/>
    </g>
    <rect x="372" y="143" width="10" height="7" fill="#fff"/>
    <path d="M373 223l4 4 4-4" stroke="#fff" fill="none"/>
    <text x="377" y="221" text-anchor="middle" font-family="Poppins,sans-serif" font-size="16" font-weight="700" fill="#fff">Kavro</text>
    <text font-family="Poppins,sans-serif" font-size="5.4" fill="#fff" text-anchor="middle"><tspan x="377" y="240">Lorem ipsum dolor sit amet, consectetur</tspan><tspan x="377" y="251">adipiscing elit, sed do eiusmod tempor</tspan><tspan x="377" y="262">incididunt ut labore et</tspan></text>
    <text font-family="Poppins,sans-serif" font-size="6.4" font-weight="600" fill="#fff" text-decoration="underline"><tspan x="344" y="281">← PRVE</tspan><tspan x="384" y="281">NEXT →</tspan></text>
  </svg>
  <span class="wheel-label" style="left:354px;top:120px;color:#8fbdf0">AGRICULTURE</span>
  <span class="wheel-label" style="left:472px;top:170px">FITNESS</span>
  <span class="wheel-label" style="left:496px;top:239px">FOOD &amp;<br>BEVERAGE</span>
  <span class="wheel-label" style="left:467px;top:304px">MINING &amp;<br>QUARRYING</span>
  <span class="wheel-label" style="left:358px;top:359px">PACKAGING</span>
  <span class="wheel-label" style="left:248px;top:313px">RECYCLING</span>
  <span class="wheel-label" style="left:237px;top:244px">WOOD</span>
  <span class="wheel-label" style="left:263px;top:170px">TILES</span>

  <span class="arrow-c" style="left:12px;top:414px"><svg viewBox="0 0 10 10"><path d="M6 2L3 5l3 3" stroke="#fff" fill="none" stroke-width="1.4"/></svg></span>
  <span class="arrow-c" style="left:537px;top:414px"><svg viewBox="0 0 10 10"><path d="M4 2l3 3-3 3" stroke="#fff" fill="none" stroke-width="1.4"/></svg></span>

  <div class="app-card">
    <div class="app-visual" role="img" aria-label="Agriculture tractor illustration"></div>
    <div class="divider"></div>
    <h3>AGRICULTURE</h3>
    <p>Lorem ipsum dolor sit amet, consectetur adipiscing elit, sed do eiusmod tempor incididunt ut labore et dolore magna aliqua. Ut enim ad minim veniam, quis nostrud exercitation ullamco laboris nisi ut aliquip ex ea commodo consequat.</p>
  </div>

  <footer class="site-footer" style="top:539px">
    <div class="f-logo">Kavro</div>
    <div class="f-social"><span class="ring"></span><span class="ring"></span></div>
    <div class="f-col" style="left:143px"><h4>QUICK LINKS</h4>Home<br>Product<br>Applications<br>Company<br>Downloads<br>Blog<br>Contact</div>
    <div class="f-col" style="left:217px"><h4>PRODUCT</h4>V-Belts<br>Ribbed Belts<br>Timing Belts<br>Thermowledable Belts<br>Agri-Belts</div>
    <div class="f-col contact" style="left:305px"><h4>CONTACT US</h4><div class="lbl">ADDRESS</div><div class="val">48 Maple Ridge Lane<br>Oakvale, ON K2P 5R1</div><div class="lbl">PHONE</div><div class="val">+ (1) 555 014 2290</div><div class="lbl">EMAIL</div><div class="val">hello@kavrodrive.com</div></div>
    <div class="f-col news" style="left:406px"><h4>NEWSLETTER</h4><p>Lorem ipsum dolor sit amet, consectetur adipiscing elit, sed do eiusmod tempor</p><div class="f-input">Enter Email <span class="go"></span></div></div>
    <div class="f-rule"></div>
    <div class="f-bottom"><span>© 2021 All Rights Reserved</span><span>PRIVACY POLICY / &nbsp;TERMS &amp; CONDITION</span></div>
  </footer>
</section>

<!-- BLOG PAGE -->
<section class="page" style="left:29px;top:851px;height:1338px">
  <div class="topbar">
    <div class="social"><span class="dot"></span><span class="dot"></span><span class="dot"></span></div>
    <span class="item"><svg viewBox="0 0 10 10"><path d="M2 1l2 2-1 1.5c.8 1.5 1.5 2.2 3 3L7.5 6l2 2L8 9.5C4 9 1 6 .5 2z" fill="#fff"/></svg>+ (1) 555 014 2290</span>
    <span class="item"><svg viewBox="0 0 10 10"><rect x="0" y="2" width="10" height="6" fill="#fff"/></svg>hello@kavrodrive.com</span>
    <span class="item">Select language: <span class="dot" style="width:6px;height:6px;background:#fff"></span> Eng ▾</span>
  </div>
  <div class="header">
    <div class="logo">Kavro</div>
    <nav class="nav"><span>Home</span><span>Product</span><span>Applications</span><span>Company</span><span>Downloads</span><span class="active">Blog</span><span>Contact</span><span>Contact</span><svg viewBox="0 0 10 10"><circle cx="4" cy="4" r="3" fill="none" stroke="#333" stroke-width="1.4"/><path d="M6.3 6.3L9 9" stroke="#333" stroke-width="1.4"/></svg></nav>
  </div>

  <h2 class="center-title" style="top:94px"><span></span>BLOG<span></span></h2>
  <p class="center-sub" style="top:121px">Lorem ipsum dolor sit amet, consectetur adipiscing,<br>sed do eiusmod tempor incididunt ut labore</p>

  <article class="b-card" style="left:70px;top:167px"><div class="b-img" role="img" aria-label="Power pylons at sunset" style="background:linear-gradient(180deg,#7a8aa0,#e98a2e 70%,#3a2a1a)"></div><div class="b-meta"><span class="avatar"></span>31-MAR-2021</div><span class="kebab"></span><h3 class="b-title">Lorem ipsum dolor sit amet, consectetur adipiscing elit, sed do eiusmod tempor</h3><p class="b-text">Sed ut perspiciatis unde omnis iste natus error sit voluptatem accusantium doloremque laudantium, totam rem aperiam, eaque ipsa quae ab illo inventore veritatis</p><div class="b-rule"></div><div class="b-foot"><span>1,531 <small>Views</small></span><span>♡ 356</span></div></article>
  <article class="b-card" style="left:292px;top:167px"><div class="b-img" role="img" aria-label="Engineers surveying near pylon at dusk" style="background:linear-gradient(180deg,#6d8db0,#f0b060 70%,#2a2a2a)"></div><div class="b-meta"><span class="avatar"></span>31-MAR-2021</div><span class="kebab"></span><h3 class="b-title">Lorem ipsum dolor sit amet, consectetur adipiscing elit, sed do eiusmod tempor</h3><p class="b-text">Sed ut perspiciatis unde omnis iste natus error sit voluptatem accusantium doloremque laudantium, totam rem aperiam, eaque ipsa quae ab illo inventore veritatis</p><div class="b-rule"></div><div class="b-foot"><span>1,531 <small>Views</small></span><span>♡ 356</span></div></article>
  <article class="b-card" style="left:70px;top:475px"><div class="b-img" role="img" aria-label="Alternator pulley close-up" style="background:linear-gradient(135deg,#c9b08a,#5a4a38)"></div><div class="b-meta"><span class="avatar"></span>31-MAR-2021</div><span class="kebab"></span><h3 class="b-title">Lorem ipsum dolor sit amet, consectetur adipiscing elit, sed do eiusmod tempor</h3><p class="b-text">Sed ut perspiciatis unde omnis iste natus error sit voluptatem accusantium doloremque laudantium, totam rem aperiam, eaque ipsa quae ab illo inventore veritatis</p><div class="b-rule"></div><div class="b-foot"><span>1,531 <small>Views</small></span><span>♡ 356</span></div></article>
  <article class="b-card" style="left:292px;top:475px"><div class="b-img" role="img" aria-label="Toothed belt held in hand" style="background:linear-gradient(135deg,#3a3a3a,#b5b5b5)"></div><div class="b-meta"><span class="avatar"></span>31-MAR-2021</div><span class="kebab"></span><h3 class="b-title">Lorem ipsum dolor sit amet, consectetur adipiscing elit, sed do eiusmod tempor</h3><p class="b-text">Sed ut perspiciatis unde omnis iste natus error sit voluptatem accusantium doloremque laudantium, totam rem aperiam, eaque ipsa quae ab illo inventore veritatis</p><div class="b-rule"></div><div class="b-foot"><span>1,531 <small>Views</small></span><span>♡ 356</span></div></article>
  <article class="b-card" style="left:70px;top:783px"><div class="b-img" role="img" aria-label="Engine belt drive with pulleys" style="background:linear-gradient(135deg,#7a7f88,#1f3f7a)"></div><div class="b-meta"><span class="avatar"></span>31-MAR-2021</div><span class="kebab"></span><h3 class="b-title">Lorem ipsum dolor sit amet, consectetur adipiscing elit, sed do eiusmod tempor</h3><p class="b-text">Sed ut perspiciatis unde omnis iste natus error sit voluptatem accusantium doloremque laudantium, totam rem aperiam, eaque ipsa quae ab illo inventore veritatis</p><div class="b-rule"></div><div class="b-foot"><span>1,531 <small>Views</small></span><span>♡ 356</span></div></article>
  <article class="b-card" style="left:292px;top:783px"><div class="b-img" role="img" aria-label="Engineer working beneath pylon" style="background:linear-gradient(160deg,#8fb4d8,#d8e4ef 60%,#e07a2a)"></div><div class="b-meta"><span class="avatar"></span>31-MAR-2021</div><span class="kebab"></span><h3 class="b-title">Lorem ipsum dolor sit amet, consectetur adipiscing elit, sed do eiusmod tempor</h3><p class="b-text">Sed ut perspiciatis unde omnis iste natus error sit voluptatem accusantium doloremque laudantium, totam rem aperiam, eaque ipsa quae ab illo inventore veritatis</p><div class="b-rule"></div><div class="b-foot"><span>1,531 <small>Views</small></span><span>♡ 356</span></div></article>

  <footer class="site-footer" style="top:1123px">
    <div class="f-logo">Kavro</div>
    <div class="f-social"><span class="ring"></span><span class="ring"></span></div>
    <div class="f-col" style="left:143px"><h4>QUICK LINKS</h4>Home<br>Product<br>Applications<br>Company<br>Downloads<br>Blog<br>Contact</div>
    <div class="f-col" style="left:217px"><h4>PRODUCT</h4>V-Belts<br>Ribbed Belts<br>Timing Belts<br>Thermowledable Belts<br>Agri-Belts</div>
    <div class="f-col contact" style="left:305px"><h4>CONTACT US</h4><div class="lbl">ADDRESS</div><div class="val">48 Maple Ridge Lane<br>Oakvale, ON K2P 5R1</div><div class="lbl">PHONE</div><div class="val">+ (1) 555 014 2290</div><div class="lbl">EMAIL</div><div class="val">hello@kavrodrive.com</div></div>
    <div class="f-col news" style="left:406px"><h4>NEWSLETTER</h4><p>Lorem ipsum dolor sit amet, consectetur adipiscing elit, sed do eiusmod tempor</p><div class="f-input">Enter Email <span class="go"></span></div></div>
    <div class="f-rule"></div>
    <div class="f-bottom"><span>© 2021 All Rights Reserved</span><span>PRIVACY POLICY / &nbsp;TERMS &amp; CONDITION</span></div>
  </footer>
</section>

<!-- DOWNLOADS PAGE -->
<section class="page" style="left:611px;top:827px;height:1200px">
  <div class="topbar">
    <div class="social"><span class="dot"></span><span class="dot"></span><span class="dot"></span></div>
    <span class="item"><svg viewBox="0 0 10 10"><path d="M2 1l2 2-1 1.5c.8 1.5 1.5 2.2 3 3L7.5 6l2 2L8 9.5C4 9 1 6 .5 2z" fill="#fff"/></svg>+ (1) 555 014 2290</span>
    <span class="item"><svg viewBox="0 0 10 10"><rect x="0" y="2" width="10" height="6" fill="#fff"/></svg>hello@kavrodrive.com</span>
    <span class="item">Select language: <span class="dot" style="width:6px;height:6px;background:#fff"></span> Eng ▾</span>
  </div>
  <div class="header">
    <div class="logo">Kavro</div>
    <nav class="nav"><span>Home</span><span>Product</span><span>Applications</span><span>Company</span><span class="active">Downloads</span><span>Blog</span><span>Contact</span><span>Contact</span><svg viewBox="0 0 10 10"><circle cx="4" cy="4" r="3" fill="none" stroke="#333" stroke-width="1.4"/><path d="M6.3 6.3L9 9" stroke="#333" stroke-width="1.4"/></svg></nav>
  </div>

  <h2 class="center-title" style="top:93px"><span></span>DOWNLOADS<span></span></h2>
  <p class="center-sub" style="top:120px">Lorem ipsum dolor sit amet, consectetur adipiscing,<br>sed do eiusmod tempor incididunt ut labore</p>

  <div class="d-img" style="left:48px;top:172px;background:linear-gradient(135deg,#f2f4f6,#b8c9d6 55%,#6f9ab8)" role="img" aria-label="Open brochure pages"></div>
  <div class="d-card" style="left:259px;top:188px"><h3>Brochure</h3><span class="tag">Get a hold of our product</span><p>Lorem ipsum dolor sit amet, consectetur adipiscing elit, sed do eiusmod tempor incididunt ut labore et dolore magna aliqua. Ut enim ad minim veniam, quis nostrud exercitation</p><div class="btn">DOWNLOAD</div></div>

  <div class="d-img" style="left:276px;top:370px;background:linear-gradient(135deg,#d9c6b8,#e9eef0 50%,#9db5a8)" role="img" aria-label="Report pulled from filing drawer"></div>
  <div class="d-card" style="left:77px;top:385px"><h3>Technical Datasheet</h3><span class="tag">Need technical information ?</span><p>Lorem ipsum dolor sit amet, consectetur adipiscing elit, sed do eiusmod tempor incididunt ut labore et dolore magna aliqua. Ut enim ad minim veniam, quis nostrud exercitation</p><div class="btn">DOWNLOAD</div></div>

  <div class="d-img" style="left:48px;top:566px;background:linear-gradient(180deg,#3f6ea8,#f0b04a 70%,#2a2a2a)" role="img" aria-label="Power pylons against sunset sky"></div>
  <div class="d-card" style="left:259px;top:582px"><h3 style="top:30px">Photos</h3><span class="tag" style="top:48px">Lorem ipsum dolor sit amet</span><p style="top:67px">Lorem ipsum dolor sit amet, consectetur adipiscing elit, sed do eiusmod tempor incididunt ut labore et dolore magna aliqua. Ut enim ad minim veniam, quis nostrud exercitation</p></div>

  <div class="d-img" style="left:276px;top:764px;background:linear-gradient(135deg,#5a5a5a,#f4f4f4 30%,#f4f4f4 60%,#d6b43a 75%,#1f2340)" role="img" aria-label="Framed certificate of appreciation"></div>
  <div class="d-card" style="left:77px;top:779px"><h3 style="top:30px">Certificate</h3><span class="tag" style="top:48px">Lorem ipsum dolor sit amet</span><p style="top:67px">Lorem ipsum dolor sit amet, consectetur adipiscing elit, sed do eiusmod tempor incididunt ut labore et dolore magna aliqua. Ut enim ad minim veniam, quis nostrud exercitation</p></div>

  <footer class="site-footer" style="top:985px">
    <div class="f-logo">Kavro</div>
    <div class="f-social"><span class="ring"></span><span class="ring"></span></div>
    <div class="f-col" style="left:143px"><h4>QUICK LINKS</h4>Home<br>Product<br>Applications<br>Company<br>Downloads<br>Blog<br>Contact</div>
    <div class="f-col" style="left:217px"><h4>PRODUCT</h4>V-Belts<br>Ribbed Belts<br>Timing Belts<br>Thermowledable Belts<br>Agri-Belts</div>
    <div class="f-col contact" style="left:305px"><h4>CONTACT US</h4><div class="lbl">ADDRESS</div><div class="val">48 Maple Ridge Lane<br>Oakvale, ON K2P 5R1</div><div class="lbl">PHONE</div><div class="val">+ (1) 555 014 2290</div><div class="lbl">EMAIL</div><div class="val">hello@kavrodrive.com</div></div>
    <div class="f-col news" style="left:406px"><h4>NEWSLETTER</h4><p>Lorem ipsum dolor sit amet, consectetur adipiscing elit, sed do eiusmod tempor</p><div class="f-input">Enter Email <span class="go"></span></div></div>
    <div class="f-rule"></div>
    <div class="f-bottom"><span>© 2021 All Rights Reserved</span><span>PRIVACY POLICY / &nbsp;TERMS &amp; CONDITION</span></div>
  </footer>
</section>

</body>
</html>
```